Business letterhead and powerpoint template

Hi, I have recently started using a new logo (found through PixelGrove) and would now like to use that logo for letterheads and powerpoint.

Attached is the logo and one version of a brochure I have recently used.

Industry/Entity Type

Business

```html
<!DOCTYPE html>
<html lang="en">
<head>
<meta charset="utf-8">
<title>Halden Capital – Letterhead and Presentation Template</title>
<link rel="stylesheet" href="https://fonts.googleapis.com/css2?family=Source+Sans+3:wght@300;400;600;700&display=swap">
<style>
  :root{
    --orange:#e4512f;
    --orange-soft:#f3a08c;
    --tint:#fbe3dc;
    --ink:#4a4a4a;
    --ink-light:#7a7a7a;
    --paper:#ffffff;
    --row:#dcdcdc;
    --bg:#e8e5e1;
  }
  *{box-sizing:border-box;margin:0;padding:0}
  html,body{width:1200px;height:811px;overflow:hidden}
  body{background:var(--bg);font-family:"Source Sans 3",Arial,sans-serif;color:var(--ink);position:relative}
  .sheet{position:absolute;width:447px;height:347px;background:var(--paper);overflow:hidden;box-shadow:0 3px 10px rgba(0,0,0,.25)}
  .sheet--letterhead{left:124px;top:36px}
  .sheet--cover{left:601px;top:36px}
  .sheet--about{left:124px;top:416px}
  .sheet--lending{left:601px;top:416px}

  .deco-circle{position:absolute;width:300px;height:300px;border-radius:50%;background:var(--tint);right:-60px;bottom:-90px}
  .sheet--letterhead .deco-circle{right:auto;left:140px;bottom:-120px;background:var(--orange);opacity:.9}

  .brand{position:absolute;display:flex;align-items:center;gap:5px;font-weight:400;color:var(--ink);letter-spacing:1px;white-space:nowrap}
  .brand__mark{width:9px;height:9px;background:var(--orange)}
  .brand--center{left:50%;top:46px;transform:translateX(-50%);font-size:19px}
  .brand--corner{right:22px;top:26px;font-size:15px}

  .top-strip{position:absolute;left:0;top:0;width:100%;height:20px;background:var(--orange)}
  .header-band{position:absolute;left:0;top:20px;width:100%;height:66px;background:#fff;box-shadow:0 4px 6px rgba(0,0,0,.18)}
  .header-rule{position:absolute;left:0;top:90px;width:100%;height:6px;background:var(--orange)}
  .letter-footer{position:absolute;left:20px;right:20px;top:322px;font-size:6.2px;font-weight:600;color:var(--ink);text-align:center;white-space:nowrap}
  .letter-footer-rule{position:absolute;left:0;top:335px;width:100%;height:3px;background:var(--orange)}

  .corner-rule{position:absolute;right:0;top:52px;width:240px;height:3px;background:linear-gradient(90deg,rgba(228,81,47,0),var(--orange-soft) 40%,var(--orange))}
  .footer-bar{position:absolute;left:0;bottom:0;width:100%;height:15px;background:var(--orange);color:#fff;font-size:5.5px;font-weight:600;text-align:right;padding:4px 10px 0 0}

  .photo{position:absolute;left:19px;width:396px;height:162px}
  .photo--gavel{top:81px;background:linear-gradient(120deg,#f1e3d3 0%,#e2c09d 45%,#a2603a 70%,#e9d3bc 100%)}
  .photo--money{top:84px;background:linear-gradient(110deg,#c9b48a 0%,#9d8560 35%,#8a4d2a 60%,#d6c39a 100%)}

  .lending-copy{position:absolute;left:19px;top:250px;width:405px;font-size:10.5px;font-weight:700;line-height:1.25;color:#2f2f2f}

  .page-title{position:absolute;left:22px;top:18px;font-size:21px;font-weight:700;color:var(--orange)}
  .col{position:absolute;top:80px}
  .col--left{left:24px;width:190px}
  .col--right{left:245px;width:180px;top:88px}
  .col h2{font-size:12px;font-weight:300;color:var(--ink);margin-bottom:12px}
  .col--right h2{font-size:10px;margin-bottom:14px}
  .col p{font-size:5.2px;line-height:1.45;color:var(--ink-light);margin-bottom:5px}
  .benefits{list-style:none}
  .benefits li{font-size:4.8px;line-height:1.4;color:var(--ink-light);margin-bottom:7px;padding-left:6px;position:relative}
  .benefits li::before{content:"";position:absolute;left:0;top:2px;width:2px;height:2px;border-radius:50%;background:var(--ink-light)}

  .services{width:100%;border-collapse:separate;border-spacing:2px;margin-top:8px}
  .services th{background:var(--orange);color:#fff;font-size:5.5px;font-weight:700;padding:3px 2px;width:50%}
  .services td{background:var(--row);font-size:4.3px;color:var(--ink-light);padding:3px 4px;height:17px;vertical-align:top}
</style>
</head>
<body>

<section class="sheet sheet--letterhead" aria-label="Letterhead">
  <div class="deco-circle"></div>
  <div class="top-strip"></div>
  <div class="header-band"></div>
  <div class="brand brand--center"><span class="brand__mark"></span>HALDEN CAPITAL</div>
  <div class="header-rule"></div>
  <p class="letter-footer">Harbourline Tower, 240 Quay Street, 12th Floor, Suite 400, Riverton | 555-014-2270 | www.haldencapital.ca</p>
  <div class="letter-footer-rule"></div>
</section>

<section class="sheet sheet--cover" aria-label="Presentation cover slide">
  <div class="deco-circle"></div>
  <div class="brand brand--corner"><span class="brand__mark"></span>HALDEN CAPITAL</div>
  <div class="corner-rule"></div>
  <div class="photo photo--gavel" role="img" aria-label="Photo of a wooden judge's gavel resting on legal papers"></div>
  <div class="footer-bar">www.haldencapital.ca</div>
</section>

<section class="sheet sheet--about" aria-label="Presentation content slide">
  <div class="deco-circle"></div>
  <h1 class="page-title">Why Use Halden Capital?</h1>
  <div class="brand brand--corner"><span class="brand__mark"></span>HALDEN CAPITAL</div>
  <div class="corner-rule"></div>

  <div class="col col--left">
    <h2>About Halden Capital</h2>
    <p>Halden Capital is a real estate focused group formed in 2009 to do two things:</p>
    <p>1. Undertake select real estate advisory services for investors who want to own regional real estate.</p>
    <p>2. Assist leading real estate investors and managers to raise institutional capital from the Asia Pacific region.</p>
    <table class="services">
      <tr><th>Regional Real Estate Advisory Services</th><th>Institutional Capital Raising</th></tr>
      <tr><td>Source off-market asset leads</td><td>Identify the right offshore partner for each mandate</td></tr>
      <tr><td>Identify assets that match investment goals</td><td>Prepare offering material and investor packs</td></tr>
      <tr><td>Undertake detailed due diligence reviews</td><td>Coordinate site visits and investor meetings</td></tr>
      <tr><td>Negotiate terms and manage the acquisition</td><td>Manage funds through approval and settlement</td></tr>
      <tr><td>Arrange debt and structuring advice</td><td>Provide ongoing reporting to every capital partner</td></tr>
      <tr><td>Project management of the full asset lifecycle</td><td>Build long term ties with regional investors</td></tr>
    </table>
  </div>

  <div class="col col--right">
    <h2>Why Use Halden Capital?</h2>
    <ul class="benefits">
      <li>Discreet, effective and fully aligned with the client's objectives.</li>
      <li>Track record in raising regional and Asian institutional capital.</li>
      <li>Track record in sourcing, acquiring, managing and divesting real estate.</li>
      <li>Halden Capital does not undertake mandates which conflict with existing clients.</li>
      <li>Strong relationships with pension funds, asset managers, family offices and banks.</li>
      <li>Strong relationships with regional real estate agents, owners and advisers.</li>
      <li>Cost effective.</li>
      <li>Personalised and tailored service to meet each client's needs.</li>
    </ul>
  </div>
  <div class="footer-bar">www.haldencapital.ca</div>
</section>

<section class="sheet sheet--lending" aria-label="Presentation closing slide">
  <div class="deco-circle"></div>
  <div class="brand brand--corner"><span class="brand__mark"></span>HALDEN CAPITAL</div>
  <div class="corner-rule"></div>
  <div class="photo photo--money" role="img" aria-label="Photo of a gavel and brass scales over banknotes"></div>
  <p class="lending-copy">Our Settlement Loans are designed to work directly with each client's needs. Get started on our fast and professional approval process to determine whether Settlement Lending is right for you.</p>
  <div class="footer-bar">www.haldencapital.ca</div>
</section>

</body>
</html>
```